Business Thank You Post Card

I would like to have a Business Thank You card designed to send to my customers. " A flat card" Front side to have some of my advertising material on it. I will provide this in the attached files. I am happy for you to pick the materials you would like to put on it. I would like for the front of the business card have this wording on it somewhere. "Thank You For Moving With KTV Haulage" I would also like for "my little Character Man" on the front to. The other side "Backside" To have the layout of a post card like the one I have provided this is for the address information. We will need to add 4 boxes on the right bottom side on the back of the card for the postcode "this can be in black & white"
Industry/Entity Type
Advertising
Look and feel
Each slider illustrates characteristics of the customer's brand and the style your logo design should communicate.

```html
<!DOCTYPE html>
<html lang="en">
<head>
<meta charset="utf-8">
<title>KTV Haulage – Thank You Postcard</title>
<link href="https://fonts.googleapis.com/css2?family=Open+Sans:wght@300;400;600;700&display=swap" rel="stylesheet">
<style>
  :root{
    --orange:#f26a21;
    --grey-band:#7c7c7c;
    --ink:#4a4a4a;
    --line:#9a9a9a;
    --white:#ffffff;
    --stage:#bfbfbf;
    --art-a:#d9b98a;
    --art-b:#f08a4b;
  }
  *{box-sizing:border-box;margin:0;padding:0}
  html,body{width:950px;height:1200px;overflow:hidden}
  body{background:var(--stage);font-family:"Open Sans",Arial,sans-serif;position:relative}

  .card{position:absolute;left:100px;width:750px;height:573px;background:var(--white);overflow:hidden;box-shadow:0 4px 14px rgba(0,0,0,.18)}
  .card--front{top:25px}
  .card--back{top:612px}

  /* front */
  .front-header{position:absolute;left:0;top:0;width:100%;height:83px;background:var(--orange);color:var(--white);
    font-size:31px;font-weight:400;display:flex;align-items:center;justify-content:center;letter-spacing:.2px}
  .front-header strong{font-weight:700;margin:0 8px}

  .brand{position:absolute;left:34px;top:106px;display:flex;align-items:center;gap:14px}
  .brand-square{width:62px;height:62px;border:3px solid var(--orange);flex:none}
  .brand-name{font-size:38px;font-weight:400;color:var(--orange);line-height:1.02;width:180px}

  .hero-art{position:absolute;left:395px;top:96px;width:345px;height:308px;border-radius:6px;
    background:radial-gradient(ellipse at 40% 60%,var(--art-b) 0%,rgba(240,138,75,.55) 30%,rgba(217,185,138,.75) 58%,var(--art-a) 100%)}

  .services{position:absolute;left:40px;top:224px;color:var(--ink)}
  .services-title{display:flex;align-items:center;gap:10px;font-size:16px;color:var(--orange);margin-bottom:14px}
  .services-title .chev{width:22px;height:22px;border-radius:50%;background:#6b6b6b;display:flex;align-items:center;justify-content:center}
  .service{display:flex;align-items:center;gap:10px;font-size:15px;height:26px}
  .service svg{flex:none}

  .tagline{position:absolute;left:0;top:412px;width:100%;height:31px;background:var(--grey-band);color:var(--white);
    font-size:14px;padding-left:38px;display:flex;align-items:center}
  .tagline span{color:var(--orange);font-weight:700;margin:0 5px}

  .contact-band{position:absolute;left:0;top:443px;width:100%;height:130px;background:var(--orange);color:var(--white)}
  .owner{position:absolute;left:36px;top:18px;font-size:13px;line-height:1.45}
  .owner-name{font-size:16px;font-weight:700}
  .owner-phone{display:flex;align-items:center;gap:8px}
  .divider{position:absolute;left:216px;top:20px;width:1px;height:92px;background:rgba(255,255,255,.8)}
  .details{position:absolute;left:242px;top:18px;font-size:12.5px;line-height:1.62}
  .details .loc{font-weight:700;font-size:13px}
  .detail{display:flex;align-items:center;gap:8px}

  /* back */
  .back-divider{position:absolute;left:372px;top:37px;width:1px;height:496px;background:var(--line)}
  .field-label{position:absolute;font-size:12px;color:#7a7a7a}
  .write-line{position:absolute;height:1px;background:var(--line)}
  .stamp-box{position:absolute;left:607px;top:37px;width:92px;height:101px;border:1px solid var(--line);
    font-size:15px;color:#9a9a9a;padding:12px 14px;line-height:1.25}
  .postcode{position:absolute;left:412px;top:418px;display:flex;gap:4px}
  .postcode-box{width:69px;height:56px;border:1px solid #7a7a7a}
</style>
</head>
<body>

<section class="card card--front">
  <header class="front-header">Thank You For Moving With <strong>KTV Haulage</strong></header>

  <div class="brand">
    <div class="brand-square"></div>
    <div class="brand-name">KTV<br>Haulage</div>
  </div>

  <div class="hero-art" role="img" aria-label="Illustrated mascot mover in orange uniform giving a thumbs up, with stacked cardboard boxes and a hand trolley"></div>

  <div class="services">
    <div class="services-title">
      <span class="chev"><svg width="10" height="10" viewBox="0 0 10 10"><path d="M3 1l4 4-4 4" fill="none" stroke="#fff" stroke-width="2"/></svg></span>
      KTV Haulage Provides:
    </div>
    <div class="service"><svg width="16" height="12" viewBox="0 0 16 12"><rect x="0" y="2" width="10" height="7" fill="#f26a21"/><rect x="10" y="4" width="5" height="5" fill="#f26a21"/><circle cx="3.5" cy="10.5" r="1.5" fill="#f26a21"/><circle cx="12" cy="10.5" r="1.5" fill="#f26a21"/></svg>Local, Country &amp; Interstate Removals</div>
    <div class="service"><svg width="16" height="14" viewBox="0 0 16 14"><path d="M1 7L8 1l7 6h-2v6H3V7z" fill="#f26a21"/></svg>Home &amp; Hi-Rise Removals</div>
    <div class="service"><svg width="16" height="14" viewBox="0 0 16 14"><rect x="2" y="3" width="12" height="10" fill="#f26a21"/><rect x="6" y="1" width="4" height="3" fill="none" stroke="#f26a21" stroke-width="1.5"/></svg>Office &amp; Factory Relocations</div>
    <div class="service"><svg width="16" height="14" viewBox="0 0 16 14"><rect x="2" y="2" width="12" height="11" fill="#f26a21"/><path d="M2 6h12" stroke="#fff" stroke-width="1.5"/></svg>Pre - Pack &amp; Unpacking Service</div>
    <div class="service"><svg width="16" height="14" viewBox="0 0 16 14"><rect x="1" y="5" width="6" height="8" fill="#f26a21"/><rect x="9" y="1" width="6" height="12" fill="#f26a21"/></svg>Storage Solutions Available</div>
  </div>

  <div class="tagline">Let <span>KTV HAULAGE</span> Take The Stress Out Of Your Next Move</div>

  <div class="contact-band">
    <div class="owner">
      <div class="owner-name">Dane Morrow</div>
      <div>Owner Operator</div>
      <div class="owner-phone">0400 318 274 <svg width="10" height="12" viewBox="0 0 10 12"><rect x="1" y="0" width="8" height="12" rx="1.5" fill="#fff"/></svg></div>
      <div class="owner-phone">07 5500 2168 <svg width="12" height="11" viewBox="0 0 12 11"><path d="M1 3h10v7H1z" fill="#fff"/><path d="M2 3c0-3 8-3 8 0" fill="none" stroke="#fff" stroke-width="1.5"/></svg></div>
    </div>
    <div class="divider"></div>
    <div class="details">
      <div class="loc">Sunport, QLD 4299</div>
      <div class="detail"><svg width="12" height="9" viewBox="0 0 12 9"><rect x="0" y="0" width="12" height="9" fill="#fff"/><path d="M0 0l6 5 6-5" fill="none" stroke="#f26a21"/></svg>hello@ktvhaulage.com</div>
      <div class="detail"><svg width="12" height="12" viewBox="0 0 12 12"><circle cx="6" cy="6" r="5.5" fill="#fff"/></svg>www.ktvhaulage.com.au</div>
      <div class="detail"><svg width="12" height="12" viewBox="0 0 12 12"><rect width="12" height="12" fill="#fff"/></svg>www.ktvhaulage.com.au/news</div>
      <div class="detail"><svg width="12" height="12" viewBox="0 0 12 12"><circle cx="6" cy="6" r="5.5" fill="#fff"/></svg>KTV Haulage</div>
    </div>
  </div>
</section>

<section class="card card--back">
  <div class="back-divider"></div>

  <div class="field-label" style="left:50px;top:216px">To</div>
  <div class="write-line" style="left:50px;top:235px;width:290px"></div>
  <div class="write-line" style="left:50px;top:292px;width:290px"></div>
  <div class="write-line" style="left:50px;top:349px;width:290px"></div>
  <div class="write-line" style="left:50px;top:406px;width:290px"></div>

  <div class="field-label" style="left:412px;top:216px">Address</div>
  <div class="write-line" style="left:412px;top:235px;width:288px"></div>
  <div class="write-line" style="left:412px;top:292px;width:288px"></div>
  <div class="write-line" style="left:412px;top:349px;width:288px"></div>

  <div class="stamp-box">Place<br>Stamp<br>Here</div>

  <div class="postcode">
    <div class="postcode-box"></div>
    <div class="postcode-box"></div>
    <div class="postcode-box"></div>
    <div class="postcode-box"></div>
  </div>
</section>

</body>
</html>
```